Brindle Oak Racquet Club app

Design a sporting app that can, post news, post events, capture and show live scores, link at least 6 websites, other functions would be an advantage. Real tennis is also known as Royal tennis and Court tennis.
This would be like a sporting clubs app that gives live scores.

Colors

Designer to choose colors to be used in the design.

Requirements
Must have
• post news, post events, capture and show live scores, link at least 6 websites,
Nice to have
• Instructions on how to launch the app on apple and android

```html
<!DOCTYPE html>
<html lang="en">
<head>
<meta charset="utf-8">
<title>Brindle Oak Racquet Club app</title>
<link href="https://fonts.googleapis.com/css2?family=Montserrat:wght@400;500;600;700;800&display=swap" rel="stylesheet">
<style>
:root{
  --page:#ffffff;
  --screen:#eef0fb;
  --card:#f6f7fd;
  --navy:#101a3d;
  --navy-soft:#24305a;
  --ink:#1b1f33;
  --muted:#6b6f86;
  --lilac:#a9a6e4;
  --line:#dfe1f0;
  --live:#e53935;
  --tab:#9ea3c0;
}
*{box-sizing:border-box;margin:0;padding:0}
html,body{width:950px;height:1200px;overflow:hidden;background:var(--page);font-family:"Montserrat",sans-serif;color:var(--ink)}
.canvas{position:relative;width:950px;height:1200px}
.screen{position:absolute;width:192px;height:412px;border-radius:18px;background:var(--screen);overflow:hidden;box-shadow:0 10px 28px rgba(16,26,61,.18)}
.screen-label{position:absolute;width:192px;text-align:center;font-size:11px;font-weight:700;letter-spacing:1.5px}
.title{text-align:center;font-size:8px;font-weight:700;letter-spacing:.5px;padding-top:20px}
.menu{position:absolute;left:12px;top:19px;width:10px}
.menu i{display:block;height:1.3px;background:var(--ink);margin-bottom:2px}
.menu i:nth-child(2){width:7px}
.hero{position:relative;height:150px;background:linear-gradient(100deg,#3a3f52 0%,#141a30 45%,#2f3448 70%,#c9ccd8 100%)}
.hero-band{position:absolute;left:0;right:0;top:52px;height:16px;background:#fff;text-align:center;font-size:8px;font-weight:800;line-height:16px}
.hero-info{position:absolute;left:0;right:0;top:74px;text-align:center;color:#fff}
.hero-round{font-size:7px;font-weight:500}
.hero-time{font-size:15px;font-weight:700;letter-spacing:1px;line-height:18px}
.live{display:inline-flex;align-items:center;gap:3px;background:var(--live);color:#fff;font-size:6px;font-weight:700;padding:1px 5px;border-radius:6px}
.live::before{content:"";width:0;height:0;border-left:4px solid #fff;border-top:2.5px solid transparent;border-bottom:2.5px solid transparent}
.section{font-size:6px;font-weight:600;padding:0 10px;margin-top:8px;color:var(--ink)}
.card{background:var(--card);margin:4px 8px;border-radius:6px;padding:6px}
.match-top{display:flex;justify-content:space-between;font-size:6px}
.match-top .tour{color:var(--lilac)}
.match-top .time{font-weight:600}
.match-row{display:flex;align-items:center;justify-content:center;gap:5px;font-size:7px;margin-top:5px}
.avatar{width:12px;height:12px;border-radius:50%;background:#9a8c84}
.vs{font-weight:700;font-size:8px;margin:0 4px}
.head-row{display:flex;justify-content:space-between;align-items:center;padding:0 10px;margin-top:8px;font-size:7.5px;font-weight:700}
.head-row span{font-size:5.5px;color:var(--lilac);font-weight:600}
.photo{margin:5px 10px 0;height:78px;border-radius:3px;background:linear-gradient(160deg,#6a3f4e 0%,#b8202a 55%,#3c2c3a 100%)}
.headline{padding:5px 10px 0;font-size:7px;font-weight:700;line-height:9px}
.subline{display:flex;justify-content:space-between;padding:2px 10px 0;font-size:6px;color:var(--muted);line-height:8px}
.subline b{color:#d9b35a;font-size:7px}
.tabbar{position:absolute;left:0;right:0;bottom:0;height:30px;background:#fff;display:flex;justify-content:space-around;align-items:center;padding:0 8px}
.tabbar::before{content:"";position:absolute;left:50%;top:-8px;width:22px;height:2px;margin-left:-11px;border-radius:2px;background:var(--ink)}
.tabbar svg{width:11px;height:11px;fill:none;stroke:var(--tab);stroke-width:1.6}
.tabbar svg.on{stroke:var(--navy)}
.tour-card{display:flex;align-items:center;gap:8px;background:#fff;margin:8px 8px 0;padding:8px;border-radius:6px 6px 0 0}
.tour-mark{width:26px;height:26px;background:#1565c0;border-radius:4px}
.tour-name{font-size:8.5px;font-weight:800;line-height:10px}
.discuss{background:#fff;margin:0 8px;padding:0 8px 8px;border-radius:0 0 6px 6px}
.discuss-row{display:flex;align-items:center;gap:5px;font-size:6.5px}
.toggle{width:9px;height:9px;border-radius:50%;border:2.5px solid #2196f3}
.faces{margin-left:auto;display:flex}
.faces i{width:8px;height:8px;border-radius:50%;background:#8d8f99;border:1px solid #fff;margin-left:-3px}
.comment{display:flex;align-items:center;gap:5px;margin-top:6px;border:1px solid var(--line);border-radius:4px;padding:3px 5px;font-size:5.5px;line-height:7px;color:var(--muted)}
.comment .avatar{width:10px;height:10px;flex:none}
.news-item{display:flex;gap:6px;padding:5px 10px 0;font-size:6px;line-height:8px}
.news-item+.news-item{border-top:1px solid var(--line);margin:4px 8px 0;padding:4px 2px 0}
.news-item time{color:var(--lilac);flex:none}
.score-big{font-size:15px}
.h2h-band{height:12px;background:var(--navy);color:#fff;font-size:7px;font-weight:700;text-align:center;line-height:12px}
.h2h{display:flex;justify-content:space-between;align-items:center;padding:8px 18px 0;font-size:7.5px;font-weight:600}
.vs-ring{width:16px;height:16px;border-radius:50%;border:1.5px solid var(--navy);font-size:6px;text-align:center;line-height:13px}
.h2h-count{text-align:center;font-size:7px;font-weight:600;letter-spacing:4px;margin-top:2px}
.games-title{text-align:center;font-size:7px;font-weight:700;margin-top:6px}
.games{width:calc(100% - 16px);margin:4px 8px 0;border-collapse:collapse;font-size:6px}
.games td{padding:2px 2px;border-bottom:1px solid var(--line)}
.games .loc{color:var(--lilac)}
.events-list{background:#fff;margin:8px 8px 0;border-radius:6px;padding:2px 8px 12px;height:318px}
.event{display:flex;align-items:center;gap:7px;padding:7px 0;border-bottom:1px solid var(--line)}
.event-mark{width:17px;height:17px;border-radius:3px;flex:none}
.event-text{flex:1;font-size:6.5px;line-height:9px}
.event-text small{display:block;font-size:5.5px;color:var(--lilac)}
.event-meta{text-align:right;font-size:5.5px;line-height:9px}
.event-meta svg{width:7px;height:7px;fill:none;stroke:var(--tab);stroke-width:1.5}
.tiles{display:grid;grid-template-columns:1fr 1fr;gap:6px;padding:50px 10px 0}
.tile{background:var(--navy);border-radius:6px;height:108px;padding:6px;color:#fff;font-size:7px;font-weight:700;position:relative}
.tile.wide{grid-column:1 / 3;height:102px;text-align:center}
.tile-art{position:absolute;left:50%;bottom:6px;transform:translateX(-50%);border-radius:4px}
.art-person{width:40px;height:76px;background:linear-gradient(180deg,#d9dbe3,#8a8fa3)}
.art-badge{width:46px;height:46px;border-radius:50%;background:#2e6b3a;bottom:26px}
.art-player{width:44px;height:74px;background:linear-gradient(180deg,#c7ccd9,#f2f3f7)}
</style>
</head>
<body>
<main class="canvas">

  <!-- HOME -->
  <section class="screen" style="left:74px;top:67px">
    <div class="hero" role="img" aria-label="Photo of two tennis players facing each other">
      <div class="menu" style="top:19px"><i></i><i></i><i></i></div>
      <div class="hero-band">GRAND COURT MASTERS</div>
      <div class="hero-info">
        <div class="hero-round">1/32 Final Court #1</div>
        <div class="hero-time">15 : 30</div>
        <span class="live">LIVE</span>
      </div>
    </div>
    <div class="card">
      <div class="section" style="padding:0;margin:0">NEXT MATCH</div>
      <div class="match-top" style="margin-top:4px"><span class="tour">GRAND COURT MASTERS</span><span class="time">21:30</span></div>
      <div class="match-row">Selma W. <i class="avatar"></i><span class="vs">VS</span><i class="avatar" style="background:#7d6a63"></i> Marta S.</div>
    </div>
    <div class="head-row">LATEST NEWS <span>SEE ALL</span></div>
    <div class="photo" role="img" aria-label="Photo of a tennis player celebrating with raised arms"></div>
    <p class="headline">Hale done it again, knocked out all all the champions in Harbor Open</p>
    <p class="subline">Rowan Hale : I am very happy with my performance <b>●</b></p>
    <nav class="tabbar">
      <svg class="on" viewBox="0 0 12 12"><path d="M2 6 6 2l4 4v5H2z"/></svg>
      <svg viewBox="0 0 12 12"><rect x="2" y="1.5" width="8" height="9" rx="1"/><path d="M4 5h4M4 7.5h4"/></svg>
      <svg viewBox="0 0 12 12"><rect x="1.5" y="1.5" width="9" height="9" rx="1"/><path d="M6 4v4M4 6h4"/></svg>
      <svg viewBox="0 0 12 12"><path d="M1.5 2h9v6H5l-2.5 2V8h-1z"/></svg>
      <svg viewBox="0 0 12 12"><rect x="1.5" y="2.5" width="9" height="8" rx="1"/><path d="M1.5 5h9M4 1v2M8 1v2"/></svg>
    </nav>
  </section>
  <div class="screen-label" style="left:74px;top:515px">HOME</div>

  <!-- NEWS -->
  <section class="screen" style="left:381px;top:67px">
    <div class="menu"><i></i><i></i><i></i></div>
    <h2 class="title">NEWS</h2>
    <div class="tour-card"><i class="tour-mark"></i><div class="tour-name">GRAND COURT<br>MASTERS</div></div>
    <div class="discuss">
      <div class="discuss-row"><i class="toggle"></i>Now discussing<span class="faces"><i></i><i></i><i></i></span></div>
      <div class="comment"><i class="avatar"></i>Venn will take this season so easily, he's real player</div>
    </div>
    <div class="section" style="margin-top:12px;font-size:7px;font-weight:700">LATEST NEWS</div>
    <div class="photo" role="img" aria-label="Photo of a tennis player celebrating with raised arms"></div>
    <p class="headline">Hale done it again, knocked out all all the champions in Harbor Open</p>
    <p class="subline">Rowan Hale : I am very happy with my performance <b>●</b></p>
    <div class="news-item" style="border-top:1px solid var(--line);margin:5px 8px 0;padding:4px 2px 0"><time>13:20</time><span>In first round he knocked out Venn and take two points lead</span></div>
    <div class="news-item"><time>09:10</time><span>In first round he knocked out Venn and take two points lead</span></div>
  </section>
  <div class="screen-label" style="left:381px;top:515px">NEWS</div>

  <!-- SCORE -->
  <section class="screen" style="left:689px;top:67px">
    <div class="hero" role="img" aria-label="Photo of two tennis players facing each other">
      <h2 class="title" style="position:absolute;left:0;right:0;top:0;color:var(--ink);background:var(--screen);padding:20px 0 6px">SCORE</h2>
      <div class="hero-band">GRAND COURT MASTERS</div>
      <div class="hero-info">
        <div class="hero-round">1/32 Final Court #1</div>
        <div class="hero-time score-big">2 : 0</div>
        <span class="live">LIVE</span>
      </div>
    </div>
    <div class="h2h-band">HEAD TO HEAD</div>
    <div class="h2h"><span>20% Wins</span><span class="vs-ring">VS</span><span>80% Wins</span></div>
    <div class="h2h-count">2 6</div>
    <div class="games-title">LAST FIVE GAMES</div>
    <table class="games">
      <tr><td>Callum</td><td>0-3</td><td>Venn</td><td class="loc">Bay Arena</td><td>8-jun-18</td></tr>
      <tr><td>Callum</td><td>1-3</td><td>Venn</td><td class="loc">Bay Arena</td><td>8-jun-18</td></tr>
      <tr><td>Callum</td><td>2-3</td><td>Venn</td><td class="loc">Bay Arena</td><td>8-jun-18</td></tr>
      <tr><td>Callum</td><td>4-1</td><td>Venn</td><td class="loc">Bay Arena</td><td>8-jun-18</td></tr>
      <tr><td>Callum</td><td>0-3</td><td>Venn</td><td class="loc">Bay Arena</td><td>8-jun-18</td></tr>
    </table>
    <div class="card" style="margin-top:6px">
      <div class="section" style="padding:0;margin:0">NEXT MATCH</div>
      <div class="match-top" style="margin-top:4px"><span class="tour">GRAND COURT MASTERS</span><span class="time">21:30</span></div>
      <div class="match-row">Selma W. <i class="avatar"></i><span class="vs">VS</span><i class="avatar" style="background:#7d6a63"></i> Marta S.</div>
    </div>
    <div class="card"><div class="match-top"><span class="tour">GRAND COURT MASTERS</span><span class="time">JUNE 19</span></div></div>
  </section>
  <div class="screen-label" style="left:689px;top:515px">SCORE</div>

  <!-- EVENTS -->
  <section class="screen" style="left:227px;top:650px">
    <h2 class="title">EVENTS</h2>
    <div class="events-list">
      <div class="event"><i class="event-mark" style="background:#4a7a2a"></i><div class="event-text">Gulf Coast Open<small>Bay City</small></div><div class="event-meta">Jan 2-6<br><svg viewBox="0 0 8 8"><path d="M2 6V3.5a2 2 0 0 1 4 0V6zM1 6h6"/></svg></div></div>
      <div class="event"><i class="event-mark" style="background:#d7e3e8"></i><div class="event-text">Harbour International<small>Port Town</small></div><div class="event-meta">Jan 1-7<br><svg viewBox="0 0 8 8"><path d="M2 6V3.5a2 2 0 0 1 4 0V6zM1 6h6"/></svg></div></div>
      <div class="event"><i class="event-mark" style="background:#1e88e5"></i><div class="event-text">Southern Open<small>River City</small></div><div class="event-meta">Jan 13-28<br><svg viewBox="0 0 8 8"><path d="M2 6V3.5a2 2 0 0 1 4 0V6zM1 6h6"/></svg></div></div>
      <div class="event"><i class="event-mark" style="background:#c9502a;border-radius:50%"></i><div class="event-text">Clay Court Open<small>Hill Park</small></div><div class="event-meta">May 26-Jun 10<br><svg viewBox="0 0 8 8"><path d="M2 6V3.5a2 2 0 0 1 4 0V6zM1 6h6"/></svg></div></div>
      <div class="event"><i class="event-mark" style="background:#4a2a6a;border-radius:50%"></i><div class="event-text">Lawn Championships<small>Green Vale</small></div><div class="event-meta">Jul 1-15<br><svg viewBox="0 0 8 8"><path d="M2 6V3.5a2 2 0 0 1 4 0V6zM1 6h6"/></svg></div></div>
      <div class="event"><i class="event-mark" style="background:#1a2a7a"></i><div class="event-text">Harbor Open<small>Eastport</small></div><div class="event-meta">Aug 26-Sep 9<br><svg viewBox="0 0 8 8"><path d="M2 6V3.5a2 2 0 0 1 4 0V6zM1 6h6"/></svg></div></div>
    </div>
    <nav class="tabbar">
      <svg viewBox="0 0 12 12"><path d="M2 6 6 2l4 4v5H2z"/></svg>
      <svg viewBox="0 0 12 12"><rect x="2" y="1.5" width="8" height="9" rx="1"/><path d="M4 5h4M4 7.5h4"/></svg>
      <svg viewBox="0 0 12 12"><rect x="1.5" y="1.5" width="9" height="9" rx="1"/><path d="M6 4v4M4 6h4"/></svg>
      <svg viewBox="0 0 12 12"><path d="M1.5 2h9v6H5l-2.5 2V8h-1z"/></svg>
      <svg class="on" viewBox="0 0 12 12"><rect x="1.5" y="2.5" width="9" height="8" rx="1"/><path d="M1.5 5h9M4 1v2M8 1v2"/></svg>
    </nav>
  </section>
  <div class="screen-label" style="left:227px;top:1098px">EVENTS</div>

  <!-- ADD -->
  <section class="screen" style="left:535px;top:650px">
    <h2 class="title">ADD</h2>
    <div class="tiles">
      <div class="tile">ADD NEWS<i class="tile-art art-person" role="img" aria-label="Illustration of a man reading a newspaper in a chair"></i></div>
      <div class="tile">ADD EVENTS<i class="tile-art art-badge" role="img" aria-label="Round tournament badge"></i></div>
      <div class="tile wide">CAPTURE A SHOT<i class="tile-art art-player" role="img" aria-label="Illustration of a tennis player holding a racquet"></i></div>
    </div>
    <nav class="tabbar">
      <svg viewBox="0 0 12 12"><path d="M2 6 6 2l4 4v5H2z"/></svg>
      <svg viewBox="0 0 12 12"><rect x="2" y="1.5" width="8" height="9" rx="1"/><path d="M4 5h4M4 7.5h4"/></svg>
      <svg class="on" viewBox="0 0 12 12"><rect x="1.5" y="1.5" width="9" height="9" rx="1"/><path d="M6 4v4M4 6h4"/></svg>
      <svg viewBox="0 0 12 12"><path d="M1.5 2h9v6H5l-2.5 2V8h-1z"/></svg>
      <svg viewBox="0 0 12 12"><rect x="1.5" y="2.5" width="9" height="8" rx="1"/><path d="M1.5 5h9M4 1v2M8 1v2"/></svg>
    </nav>
  </section>
  <div class="screen-label" style="left:535px;top:1098px">ADD</div>

</main>
</body>
</html>
```